Business Card Design

We are a flooring/granite/cabinet company
want a sleek and modern design card. Will send our logo. maybe our logo in 3d on card.
black card

Industry/Entity Type

Business

Contact Information for Business Card

Daniel Restrepo
company name Stonecrest Tile Depot
4728 loop 60w 78419
210-647-3928
stonecresttiledepot@mailbarn.net

```html
<!DOCTYPE html>
<html lang="en">
<head>
<meta charset="utf-8">
<title>Stonecrest Tile Depot – Business Card</title>
<link rel="stylesheet" href="https://fonts.googleapis.com/css2?family=Open+Sans:ital,wght@0,400;0,600;1,400&display=swap">
<style>
  :root {
    --card-black: #0b0b0b;
    --card-glow: #2a2a2a;
    --brand-blue: #1d4a72;
    --accent-red: #e31b23;
    --ink: #1e1e1e;
    --paper: #ffffff;
    --light-text: #f2f2f2;
  }
  * { box-sizing: border-box; margin: 0; padding: 0; }
  html, body {
    width: 1017px; height: 1200px; overflow: hidden;
    background: var(--paper);
    font-family: "Open Sans", Arial, sans-serif;
  }
  .canvas { position: relative; width: 1017px; height: 1200px; }

  .card-front {
    position: absolute; left: 0; top: 0; width: 1017px; height: 595px;
    background: radial-gradient(ellipse 55% 70% at 50% 38%, var(--card-glow) 0%, #151515 45%, var(--card-black) 100%);
    display: flex; align-items: center; justify-content: center;
  }
  .accent-band {
    position: absolute; left: 0; top: 595px; width: 1017px; height: 10px;
    background: var(--accent-red);
  }
  .card-back-brand {
    position: absolute; left: 0; top: 605px; width: 430px; height: 595px;
    background: radial-gradient(ellipse 80% 55% at 50% 45%, #262626 0%, #141414 55%, var(--card-black) 100%);
  }
  .card-back-details {
    position: absolute; left: 430px; top: 605px; width: 587px; height: 595px;
    background: var(--paper);
  }

  .brand-name {
    display: flex; align-items: center; gap: 14px;
    color: var(--brand-blue); font-weight: 600; white-space: nowrap;
  }
  .brand-mark { width: 0.7em; height: 0.7em; background: var(--brand-blue); flex: none; }
  .card-front .brand-name { font-size: 46px; margin-top: 10px; }

  .card-back-brand .brand-name {
    position: absolute; left: 0; width: 430px; top: 242px;
    justify-content: center; font-size: 28px; gap: 10px;
  }
  .address {
    position: absolute; left: 0; width: 430px; top: 327px;
    text-align: center; color: var(--light-text); font-size: 23px;
  }

  .person-name {
    position: absolute; left: 53px; top: 195px;
    font-size: 54px; font-weight: 400; color: var(--ink); line-height: 1;
  }
  .person-role {
    position: absolute; left: 57px; top: 256px;
    font-size: 33px; font-style: italic; color: var(--ink); line-height: 1;
  }
  .contact-list {
    position: absolute; left: 58px; top: 326px; list-style: none;
    font-size: 23px; color: var(--ink); line-height: 29px;
  }
  .contact-list li { display: flex; align-items: center; gap: 9px; }
  .contact-list svg { width: 22px; height: 20px; fill: var(--ink); flex: none; }
</style>
</head>
<body>
<main class="canvas">
  <section class="card-front">
    <div class="brand-name"><span class="brand-mark"></span>Stonecrest Tile Depot</div>
  </section>

  <div class="accent-band"></div>

  <section class="card-back-brand">
    <div class="brand-name"><span class="brand-mark"></span>Stonecrest Tile Depot</div>
    <p class="address">4728 loop 60w 78419</p>
  </section>

  <section class="card-back-details">
    <h1 class="person-name">Daniel Restrepo</h1>
    <p class="person-role">Manager</p>
    <ul class="contact-list">
      <li>
        <svg viewBox="0 0 24 24" aria-hidden="true"><path d="M6.6 10.8a15.1 15.1 0 0 0 6.6 6.6l2.2-2.2a1 1 0 0 1 1-.25 11.4 11.4 0 0 0 3.6.57 1 1 0 0 1 1 1V20a1 1 0 0 1-1 1A17 17 0 0 1 3 4a1 1 0 0 1 1-1h3.5a1 1 0 0 1 1 1c0 1.25.2 2.45.57 3.57a1 1 0 0 1-.25 1z"/></svg>
        210-647-3928
      </li>
      <li>
        <svg viewBox="0 0 24 20" aria-hidden="true"><path d="M1 2h22v2L12 11 1 4z"/><path d="M1 6.5l11 7 11-7V18H1z"/></svg>
        stonecresttiledepot@mailbarn.net
      </li>
    </ul>
  </section>
</main>
</body>
</html>
```